HANDYMAN SERVICES

we provide a good,and reliable service.we do all aspects of home improvement ,also all garden services,and any repairs,no job too small,free quotes .
I am aiming towards the general public for clients,also be doing special rates for the elderly,and reducing the price for anyone who does a friend reference. It will be free quotes/consultation,all work will be guaranteed.
Now the type of work we do is cctv installation,decking,patio/driveway cleaning,garages for erecting/repairs,house/garage clearances,fit alarm systems,fit or repair windows/doors,lay patios,repair roofs,decorate interior/external,erect ariaels,lay driveways,erect or repair fencing,lay drainage,repair or erect guttering and soffits,water features,erect or repair kitchens/bathrooms,also plastering,lay lawns or repair,also repair/erect sheds.
Home Improvement

```html
<!DOCTYPE html>
<html lang="en">
<head>
<meta charset="utf-8">
<title>Handyman Service Flyer</title>
<link rel="stylesheet" href="https://fonts.googleapis.com/css2?family=Gelasio:wght@700&family=Source+Sans+3:wght@400&display=swap">
<style>
  :root {
    --navy: #243a8c;
    --ink: #2b2f78;
    --cyan: #00aeef;
    --band: #5b5fa6;
    --white: #ffffff;
    --photo-light: #f6f6f6;
    --photo-mid: #e4e2de;
    --photo-dark: #b9bcc4;
  }
  html, body {
    margin: 0;
    padding: 0;
    width: 1200px;
    height: 1000px;
    overflow: hidden;
    background: var(--white);
  }
  .flyer {
    position: absolute;
    left: 108px;
    top: 147px;
    width: 992px;
    height: 698px;
    overflow: hidden;
    font-family: "Source Sans 3", "Helvetica Neue", Arial, sans-serif;
  }
  .flyer__photo {
    position: absolute;
    inset: 0;
    background:
      radial-gradient(ellipse 260px 420px at 700px 330px, rgba(120,130,170,0.45), rgba(120,130,170,0) 70%),
      linear-gradient(90deg, var(--photo-light) 0%, var(--photo-light) 40%, var(--photo-mid) 62%, var(--photo-dark) 100%);
  }
  .flyer__title {
    position: absolute;
    left: 55px;
    top: 30px;
    margin: 0;
    font-family: "Gelasio", Georgia, serif;
    font-weight: 700;
    font-size: 64px;
    line-height: 1.1;
    color: var(--navy);
    letter-spacing: 0.3px;
  }
  .flyer__title-accent { color: var(--cyan); }
  .flyer__intro {
    position: absolute;
    left: 55px;
    top: 136px;
    width: 470px;
    margin: 0;
    font-family: "Gelasio", Georgia, serif;
    font-weight: 700;
    font-size: 26px;
    line-height: 35px;
    color: var(--ink);
  }
  .flyer__perks {
    position: absolute;
    left: 55px;
    top: 290px;
    margin: 0;
    padding: 0;
    list-style: none;
    font-size: 21px;
    line-height: 30px;
    color: var(--ink);
  }
  .flyer__perks li {
    position: relative;
    padding-left: 28px;
  }
  .flyer__perks li::before {
    content: "";
    position: absolute;
    left: 3px;
    top: 12px;
    width: 6px;
    height: 6px;
    border-radius: 50%;
    background: var(--cyan);
  }
  .flyer__services {
    position: absolute;
    left: 0;
    top: 469px;
    width: 992px;
    height: 173px;
    box-sizing: border-box;
    padding-top: 14px;
    background: rgba(82, 86, 160, 0.9);
    color: var(--white);
    text-align: center;
    font-size: 19px;
    line-height: 27px;
  }
  .flyer__services p { margin: 0; white-space: nowrap; }
  .flyer__cta {
    position: absolute;
    left: 0;
    top: 642px;
    width: 992px;
    height: 56px;
    background: var(--cyan);
    color: var(--white);
    font-family: "Gelasio", Georgia, serif;
    font-weight: 700;
    font-size: 25px;
    line-height: 56px;
    box-sizing: border-box;
    padding-left: 62px;
    margin: 0;
  }
</style>
</head>
<body>
  <main class="flyer">
    <div class="flyer__photo" role="img" aria-label="Photo of a smiling handyman in a yellow hard hat and blue checked shirt carrying timber planks in a bright interior"></div>

    <h1 class="flyer__title">Handyman <span class="flyer__title-accent">Service</span></h1>

    <p class="flyer__intro">We provide a good, reliable service that covers all aspects of home improvement, garden services and any repairs.</p>

    <ul class="flyer__perks">
      <li>No job is too small</li>
      <li>Special rates for the Senior Citizens<br>and friend referrals</li>
      <li>Free quotes and consultations</li>
      <li>All work is guaranteed</li>
    </ul>

    <section class="flyer__services">
      <p>CCTV and alarm installation &nbsp;•&nbsp; Decking &nbsp;•&nbsp; Patios &nbsp;•&nbsp; Driveway cleaning</p>
      <p>Fitting or repairing windows and doors &nbsp;•&nbsp; Garage/shed erecting and repairs &nbsp;•&nbsp; Roof repairs</p>
      <p>House/garage clearances &nbsp;•&nbsp; Decorating, interior and external &nbsp;•&nbsp; Erecting aerials &nbsp;•&nbsp; Laying driveways</p>
      <p>Fence erection or repair &nbsp;•&nbsp; Lay drainage, repairing or erecting guttering and soffits &nbsp;•&nbsp; Water features</p>
      <p>Kitchen and bathroom fitting or repairs &nbsp;•&nbsp; Plastering &nbsp;•&nbsp; Lawn laying</p>
    </section>

    <p class="flyer__cta">For more information or a free quote please call 07700 900123</p>
  </main>
</body>
</html>
```